Solar panel cleaning flyer design.

I'm looking for a flyer design for my new company called Brightwell Panel Works. We are a South Australian company that professionally clean residential and commercial solar panels. We generate leads by going door to door and need a flyer to hand out to our customers if they are interested in our service. As we are a new company we don't have anything particular in mind so be creative! Must include the company name and logo.

Industry/Entity Type

It Company

```html
<!DOCTYPE html>
<html lang="en">
<head>
<meta charset="UTF-8">
<title>Brightwell Panel Works – Flyer</title>
<link href="https://fonts.googleapis.com/css2?family=Montserrat:ital,wght@0,600;1,600&family=Raleway:wght@300;400;700&display=swap" rel="stylesheet">
<style>
  :root {
    --page-bg: #ebe8e3;
    --paper: #ffffff;
    --green-light: #8dc63f;
    --green-dark: #6a9a2e;
    --blue: #2b7fc3;
    --ink: #2f2f2f;
    --band-grey: #d5d6d8;
    --sky-top: #2462c8;
    --sky-mid: #3f86d8;
    --cloud: #dbe7f3;
    --panel-blue: #1c3d94;
    --panel-deep: #132c73;
  }
  * { margin: 0; padding: 0; box-sizing: border-box; }
  html, body { width: 900px; height: 1200px; overflow: hidden; }
  body { background: var(--page-bg); font-family: "Raleway", sans-serif; position: relative; }

  .flyer {
    position: absolute; left: 82px; top: 88px;
    width: 730px; height: 1034px;
    background: var(--paper);
  }
  .hero-photo {
    position: absolute; left: 25px; top: 24px;
    width: 680px; height: 436px;
    background:
      radial-gradient(ellipse 340px 70px at 200px 270px, rgba(232,240,249,0.85), rgba(232,240,249,0) 100%),
      radial-gradient(ellipse 260px 45px at 420px 300px, rgba(220,232,245,0.7), rgba(220,232,245,0) 100%),
      radial-gradient(ellipse 120px 18px at 140px 12px, rgba(230,238,248,0.7), rgba(230,238,248,0) 100%),
      linear-gradient(180deg, var(--sky-top) 0%, var(--sky-mid) 45%, #7fb0e4 66%, var(--panel-blue) 74%, #2a55b4 86%, var(--panel-deep) 100%);
  }
  .intro-band {
    position: absolute; left: 25px; top: 460px;
    width: 680px; height: 182px;
    background: linear-gradient(180deg, var(--green-light) 0%, var(--green-dark) 100%);
    color: #fff;
  }
  .intro-band .kicker {
    position: absolute; left: 25px; top: 40px;
    font-family: "Montserrat", sans-serif; font-style: italic; font-weight: 600;
    font-size: 26px; line-height: 1.2;
  }
  .intro-band .headline {
    position: absolute; left: 24px; top: 82px;
    font-family: "Montserrat", sans-serif; font-weight: 600;
    font-size: 70px; line-height: 1;
  }
  .divider { position: absolute; width: 3px; background: #fff; }
  .intro-band .divider { left: 266px; top: 22px; height: 142px; }
  .intro-band .summary {
    position: absolute; left: 298px; top: 28px;
    font-size: 18.6px; line-height: 23.6px; font-weight: 300; white-space: nowrap;
  }

  .brand {
    position: absolute; left: 40px; top: 770px;
    width: 250px; display: flex; align-items: center; justify-content: center; gap: 10px;
    transform: translateY(-50%);
  }
  .brand-dot { width: 26px; height: 26px; border-radius: 50%; background: var(--blue); flex: none; }
  .brand-name {
    font-family: "Raleway", sans-serif; font-weight: 700;
    font-size: 27px; line-height: 1.1; color: var(--blue);
  }
  .about-text {
    position: absolute; left: 323px; top: 682px;
    font-size: 18.6px; line-height: 23.4px; color: var(--ink); white-space: nowrap;
  }

  .contact-band {
    position: absolute; left: 25px; top: 912px;
    width: 680px; height: 97px;
    background: var(--band-grey);
  }
  .contact-band .label {
    position: absolute; left: 25px; top: 40px;
    font-size: 22px; color: #3a3a3a; font-weight: 400;
  }
  .contact-band .label strong { color: var(--blue); font-weight: 700; }
  .contact-band .divider { left: 266px; top: 14px; height: 70px; }
  .contact-list {
    position: absolute; left: 296px; top: 17px; list-style: none;
    font-size: 16.5px; color: #2a2a2a;
  }
  .contact-list li { display: flex; align-items: center; gap: 6px; height: 24px; }
  .contact-list svg { width: 15px; height: 15px; flex: none; }

  .footer-strip {
    position: absolute; left: 0; top: 1009px;
    width: 730px; height: 25px; background: var(--green-light);
  }
</style>
</head>
<body>
  <div class="flyer">
    <div class="hero-photo" role="img" aria-label="Photo of a technician in a helmet and harness cleaning rooftop solar panels with a long pole brush under a blue sky"></div>

    <section class="intro-band">
      <p class="kicker">Specializing in</p>
      <p class="headline">100%</p>
      <span class="divider"></span>
      <p class="summary">We are a South Australian company<br>that professionally clean residential and<br>commercial solar panels. We generate<br>leads by going door to door and need a<br>flyer to hand out to our customers if they<br>are interested in our service.</p>
    </section>

    <div class="brand">
      <span class="brand-dot"></span>
      <span class="brand-name">Brightwell<br>Panel Works</span>
    </div>

    <p class="about-text">Re necatistio temque apictotatur assi dis<br>dipsant.Arciend aerferspid quiducius alit,<br>conectas elia que consentum quatem-<br>quiam fugiat dereiciae pres aut eatur re,<br>etur auditiis eossunt mos aborrovid mo-<br>diore magnihit, omniendaecae eos sedit<br>qui berior si dentiat ent.Torrum si audit,<br>od elibusd antibus sedis platem</p>

    <section class="contact-band">
      <p class="label">CONTACT <strong>US</strong>:</p>
      <span class="divider"></span>
      <ul class="contact-list">
        <li>
          <svg viewBox="0 0 16 16" aria-hidden="true"><circle cx="8" cy="8" r="8" fill="#2b7fc3"/><path d="M5.2 4.2l1.4-.2.8 2-1 .8c.5 1.1 1.2 1.8 2.3 2.3l.8-1 2 .8-.2 1.4c-3.4.2-6.3-2.7-6.1-6.1z" fill="#fff"/></svg>
          <span>0412 555 018</span>
        </li>
        <li>
          <svg viewBox="0 0 16 16" aria-hidden="true"><circle cx="8" cy="8" r="8" fill="#2b7fc3"/><rect x="4" y="5" width="8" height="6" rx="1" fill="#fff"/><path d="M4.3 5.4L8 8.3l3.7-2.9" stroke="#2b7fc3" stroke-width="1" fill="none"/></svg>
          <span>info@brightwellpanel.com.au</span>
        </li>
        <li>
          <svg viewBox="0 0 16 16" aria-hidden="true"><circle cx="8" cy="8" r="8" fill="#2b7fc3"/><circle cx="8" cy="8" r="4.5" stroke="#fff" stroke-width="1" fill="none"/><ellipse cx="8" cy="8" rx="2" ry="4.5" stroke="#fff" stroke-width="1" fill="none"/><path d="M3.5 8h9" stroke="#fff" stroke-width="1"/></svg>
          <span>www.brightwellpanel.com.au</span>
        </li>
      </ul>
    </section>

    <div class="footer-strip"></div>
  </div>
</body>
</html>
```